Quorvel Business Card

Looking for business card ideas. Company name is Quorvel. Have a few basic ideas on attachment. Please submit anything with the logo and general information from attachment.

Industry/Entity Type

Business

```html
<!DOCTYPE html>
<html lang="en">
<head>
<meta charset="utf-8">
<title>Quorvel Business Card</title>
<link rel="stylesheet" href="https://fonts.googleapis.com/css2?family=Montserrat:wght@400;700&display=swap">
<style>
  :root {
    --page-bg: #ffffff;
    --card-bg: #ffffff;
    --card-edge: #d9d9d9;
    --ink: #111111;
    --brand-red: #e60000;
  }
  * { margin: 0; padding: 0; box-sizing: border-box; }
  html, body {
    width: 1200px;
    height: 666px;
    overflow: hidden;
    background: var(--page-bg);
  }
  .canvas {
    position: relative;
    width: 1200px;
    height: 666px;
    font-family: "Montserrat", Arial, sans-serif;
    color: var(--ink);
  }
  .card {
    position: absolute;
    left: 88px;
    top: 60px;
    width: 1027px;
    height: 535px;
    background: var(--card-bg);
    border: 3px solid var(--card-edge);
  }
  .tagline {
    position: absolute;
    left: 0;
    right: 0;
    top: 101px;
    text-align: center;
    font-weight: 700;
    font-size: 36px;
    line-height: 44px;
  }
  .brand {
    position: absolute;
    left: 0;
    right: 0;
    top: 172px;
    text-align: center;
  }
  .brand-name {
    font-weight: 700;
    font-size: 124px;
    line-height: 150px;
    color: var(--brand-red);
    letter-spacing: 6px;
  }
  .person {
    position: absolute;
    left: 0;
    right: 0;
    top: 358px;
    text-align: center;
    font-weight: 400;
    font-size: 42px;
    line-height: 52px;
  }
  .contact {
    position: absolute;
    top: 449px;
    font-style: normal;
    font-weight: 400;
    font-size: 33px;
    line-height: 34px;
    white-space: nowrap;
  }
  .contact-phone-mail { left: 162px; text-align: left; }
  .contact-address { right: 160px; text-align: right; }
</style>
</head>
<body>
  <main class="canvas">
    <section class="card"></section>

    <p class="tagline">Leading churches to the Next level</p>

    <div class="brand">
      <span class="brand-name">Quorvel</span>
    </div>

    <p class="person">Dana Merrow, Dir.</p>

    <address class="contact contact-phone-mail">
      (555) 310-4826 Office<br>
      (555) 274-9053 Cell<br>
      dmerrow@quorvel.com
    </address>

    <address class="contact contact-address">
      2840 S. Larkin Ave.<br>
      Marlow, TX 79841<br>
      www.quorvel.org
    </address>
  </main>
</body>
</html>
```